Marketing Collateral for Construction Company
Keystone Cellar Craftworks
Attention Designers:
I have uploaded a number of pictures of basement project that our company has done. Please use these pictures where you think they will work in the designs for the marketing peripherals.
Thank you,
Mark
where is the content for the flyer and brochure?
@QW - please check your private messages on top right corner once you login to your account & reply. Thanks
Designers,
I have changed the scope of the project only to include:
-tri-fold brochure
-flyer
-door hanger
I have also uploaded AI files for you to use in your designs. Please let me know if you need more source files or a different format.
Thanks,

```html
<!DOCTYPE html>
<html lang="en">
<head>
<meta charset="utf-8">
<title>Keystone Cellar Craftworks – Collateral</title>
<link href="https://fonts.googleapis.com/css2?family=Open+Sans:ital,wght@0,400;0,700;1,700&family=Oswald:wght@500&display=swap" rel="stylesheet">
<style>
  :root{
    --backdrop:#4a3324;
    --paper:#ffffff;
    --green:#3f8c2b;
    --green-dark:#22611a;
    --green-light:#6fb03c;
    --blue:#2d46a0;
    --photo-warm:#8a5a2c;
    --photo-deep:#3d2412;
    --photo-light:#c79a5c;
    --body-text:#2d2d2d;
    --label:#f1ece4;
  }
  *{box-sizing:border-box;margin:0;padding:0}
  html,body{width:1200px;height:754px;overflow:hidden;background:var(--backdrop)}
  .canvas{position:relative;width:1200px;height:754px;overflow:hidden;background:var(--backdrop);font-family:"Open Sans",Arial,sans-serif}
  .piece{position:absolute;background:var(--paper);overflow:hidden;box-shadow:0 3px 8px rgba(0,0,0,.45)}
  .piece svg.shapes{position:absolute;inset:0;width:100%;height:100%}
  .photo{position:absolute;background:linear-gradient(160deg,var(--photo-light),var(--photo-warm) 45%,var(--photo-deep))}
  .brand{position:absolute;display:flex;align-items:center;gap:4px;color:var(--green);font-weight:700;font-size:9px;line-height:1.1}
  .brand .dot{width:9px;height:9px;border-radius:50%;background:var(--green);flex:none}
  .heading{position:absolute;color:var(--green);font-weight:700;font-size:13px;line-height:1}
  .heading.on-green{color:var(--paper)}
  .copy{position:absolute;font-size:5.6px;line-height:1.45;color:var(--body-text)}
  .copy.on-green{color:var(--paper)}
  .copy p+p{margin-top:4px}
  .tagline{position:absolute;font-family:"Oswald",sans-serif;font-weight:500;text-transform:uppercase;color:var(--paper);font-size:10px;line-height:1.15;letter-spacing:.5px}
  .tagline.green{color:var(--green)}
  .site{position:absolute;font-size:5.5px;color:var(--green-dark);font-weight:700}
  .label{position:absolute;font-style:italic;font-weight:700;color:var(--label);font-size:11px;letter-spacing:.5px;text-transform:uppercase;line-height:1.3}
  .hole{position:absolute;border-radius:50%;background:var(--backdrop)}
  .slit{position:absolute;background:var(--backdrop);width:2px}
</style>
</head>
<body>
<div class="canvas">

  <!-- Tri-fold brochure, outside -->
  <section class="piece brochure-outside" style="left:19px;top:7px;width:305px;height:288px">
    <svg class="shapes" viewBox="0 0 305 288" preserveAspectRatio="none" aria-hidden="true">
      <path d="M0 0H10Q4 14 0 22Z" fill="var(--green)"/>
      <path d="M0 150Q50 200 102 170V288H0Z" fill="var(--green)"/>
      <path d="M0 146Q50 196 102 166" fill="none" stroke="var(--blue)" stroke-width="2"/>
      <path d="M203 0H305V288H260Q300 150 203 80Z" fill="var(--green-dark)"/>
      <path d="M203 78Q300 150 258 288" fill="none" stroke="var(--blue)" stroke-width="2"/>
      <path d="M175 0H203V288H185Q215 140 175 0Z" fill="var(--green)"/>
    </svg>
    <div class="brand" style="left:12px;top:12px"><span class="dot"></span></div>
    <div class="heading" style="left:25px;top:9px">Us<br>About</div>
    <div class="copy" style="left:8px;top:44px;width:88px"><p>We finish basements with care, turning bare concrete into warm rooms your family will use every day.</p></div>
    <div class="photo" style="left:30px;top:96px;width:72px;height:110px" role="img" aria-label="Photo of a finished basement bar with wood cabinetry"></div>
    <div class="tagline" style="left:8px;top:226px">Form<br>Following<br>Function</div>

    <div class="brand" style="left:112px;top:15px"><span class="dot"></span></div>
    <div class="heading" style="left:124px;top:16px">Services</div>
    <div class="copy" style="left:110px;top:40px;width:66px"><p>We finish basements with care, turning bare concrete into warm rooms your family will use every day.</p><p>Our crew plans, frames, wires and trims each space to fit how you live and entertain.</p></div>
    <div class="brand" style="left:110px;top:200px;width:66px"><span class="dot"></span>Keystone Cellar Craftworks</div>
    <div class="site" style="left:110px;top:262px">www.keystonecellarcraft.com</div>

    <div class="photo" style="left:203px;top:60px;width:70px;height:228px" role="img" aria-label="Photo of a finished basement staircase"></div>
    <div class="tagline" style="left:212px;top:110px">Form<br>Following<br>Function</div>
  </section>

  <!-- Tri-fold brochure, inside -->
  <section class="piece brochure-inside" style="left:19px;top:317px;width:305px;height:365px">
    <svg class="shapes" viewBox="0 0 305 365" preserveAspectRatio="none" aria-hidden="true">
      <path d="M0 0H12Q5 12 0 18Z" fill="var(--green)"/>
      <path d="M0 260Q60 230 102 300V365H0Z" fill="var(--green)"/>
      <path d="M0 255Q60 225 102 295" fill="none" stroke="var(--blue)" stroke-width="2"/>
      <path d="M102 0H130Q118 10 102 16Z" fill="var(--green)"/>
      <path d="M102 230Q150 200 203 240V365H102Z" fill="var(--green)"/>
      <path d="M102 226Q150 196 203 236" fill="none" stroke="var(--blue)" stroke-width="2"/>
      <path d="M203 0H305V80Q250 40 203 90Z" fill="var(--green-dark)"/>
    </svg>
    <div class="brand" style="left:12px;top:25px"><span class="dot"></span></div>
    <div class="heading" style="left:25px;top:22px">Us<br>About</div>
    <div class="copy" style="left:8px;top:56px;width:88px"><p>We finish basements with care, turning bare concrete into warm rooms your family will use every day.</p><p>Our crew plans, frames, wires and trims each space to fit how you live and entertain.</p><p>Call for a free visit and a clear estimate.</p></div>
    <div class="tagline" style="left:8px;top:300px">Form<br>Following<br>Function</div>

    <div class="brand" style="left:112px;top:28px"><span class="dot"></span></div>
    <div class="heading" style="left:124px;top:27px">Services</div>
    <div class="copy" style="left:110px;top:50px;width:86px"><p>Our crew plans, frames, wires and trims each space to fit how you live and entertain.</p><p>Call for a free visit and a clear estimate.</p></div>

    <div class="photo" style="left:203px;top:90px;width:102px;height:275px" role="img" aria-label="Photo of basement library shelving with warm lighting"></div>
  </section>
  <div class="label" style="left:150px;top:690px">Brochure</div>

  <!-- Flyer -->
  <section class="piece flyer" style="left:336px;top:7px;width:300px;height:413px">
    <svg class="shapes" viewBox="0 0 300 413" preserveAspectRatio="none" aria-hidden="true">
      <path d="M0 0H14Q6 18 0 28Z" fill="var(--green)"/>
      <path d="M0 230Q120 180 170 260Q200 330 300 300V413H0Z" fill="var(--green)"/>
      <path d="M170 413Q180 320 300 290V413Z" fill="var(--green-dark)"/>
      <path d="M0 225Q120 175 170 255Q200 325 300 295" fill="none" stroke="var(--blue)" stroke-width="2"/>
    </svg>
    <div class="brand" style="left:16px;top:18px;width:90px;font-size:11px"><span class="dot" style="width:12px;height:12px"></span>Keystone Cellar Craftworks</div>
    <div class="tagline green" style="left:120px;top:18px;font-size:11px">Form<br>Following<br>Function</div>
    <div class="copy" style="left:14px;top:66px;width:270px;font-size:6px"><p>We finish basements with care, turning bare concrete into warm rooms your family will use every day. Our crew plans, frames, wires and trims each space to fit how you live and entertain.</p><p>Call for a free visit and a clear estimate.</p></div>
    <div class="copy" style="left:170px;top:150px;width:118px;font-size:6px"><p>Our crew plans, frames, wires and trims each space to fit how you live and entertain.</p></div>
    <div class="photo" style="left:0;top:236px;width:160px;height:177px" role="img" aria-label="Photo of a finished basement bar with stools"></div>
  </section>
  <div class="label" style="left:690px;top:436px">Flyer</div>

  <!-- Door hanger, front -->
  <section class="piece door-hanger-front" style="left:732px;top:7px;width:115px;height:570px;background:var(--green)">
    <svg class="shapes" viewBox="0 0 115 570" preserveAspectRatio="none" aria-hidden="true">
      <path d="M0 0H115V250Q60 200 0 240Z" fill="var(--green-dark)"/>
      <path d="M115 140Q60 300 115 420Z" fill="var(--paper)"/>
      <path d="M115 136Q56 300 115 424" fill="none" stroke="var(--blue)" stroke-width="2"/>
    </svg>
    <div class="hole" style="left:22px;top:18px;width:70px;height:70px"></div>
    <div class="slit" style="left:56px;top:0;height:20px"></div>
    <div class="heading on-green" style="left:12px;top:150px;font-size:15px">Us<br>About</div>
    <div class="copy on-green" style="left:10px;top:260px;width:66px"><p>We finish basements with care, turning bare concrete into warm rooms your family will use every day.</p></div>
  </section>

  <!-- Door hanger, back -->
  <section class="piece door-hanger-back" style="left:852px;top:7px;width:118px;height:570px">
    <svg class="shapes" viewBox="0 0 118 570" preserveAspectRatio="none" aria-hidden="true">
      <path d="M0 0H20Q0 150 0 200Z" fill="var(--green)"/>
      <path d="M0 220Q70 260 118 200V570H0Z" fill="var(--green)"/>
      <path d="M0 215Q70 255 118 195" fill="none" stroke="var(--blue)" stroke-width="2"/>
      <path d="M60 570Q90 420 118 400V570Z" fill="var(--green-dark)"/>
    </svg>
    <div class="hole" style="left:24px;top:18px;width:70px;height:70px"></div>
    <div class="slit" style="left:58px;top:0;height:20px"></div>
    <div class="brand" style="left:12px;top:110px;width:96px;font-size:10px"><span class="dot" style="width:11px;height:11px"></span>Keystone Cellar Craftworks</div>
    <div class="copy" style="left:10px;top:146px;width:98px"><p>Our crew plans, frames, wires and trims each space to fit how you live and entertain.</p></div>
    <div class="copy on-green" style="left:10px;top:252px;width:98px"><p>We finish basements with care, turning bare concrete into warm rooms your family will use every day.</p><p>Our crew plans, frames, wires and trims each space to fit how you live and entertain.</p><p>Call for a free visit and a clear estimate.</p></div>
  </section>
  <div class="label" style="left:850px;top:724px">Door Hanger<br>Front/Back</div>

</div>
</body>
</html>
```